Business Card for Multi-Brand Sportswear Company

We are looking for a business card which represents our company and the multiple brands within it.

The company: Kelt Athletic (LTD)
The brands: Kelt, PawaLuni, VerdantFlex, Grit and Gale

Employees using these cards would be representing Kelt Athletic, rather than any of the individual brands. You will see a current design within the uploaded files, to give some inspiration. The actual text of the brands is not necessary, but the logos should be on there is some format.

Our creative minds on this are stretched, so we are looking for someone to make this their own, and show us what a good business card should look like.

We may like to get these printed with spot gloss, so keep that in mind with your designs.

www.keltathletic.co.uk

Industry/Entity Type

Business

Contact Information for Business Card

Tom Hollingsworth-Pryce
Operations Manager
(+44) 1632 960 418
Tom@keltathletic.co.uk
www.keltathletic.co.uk

Font styles to use
Sans Serif
Other font styles liked:
• Eurostile

Colors
ffffff

Requirements
Nice to have
• Dark (black) background

```html
<!DOCTYPE html>
<html lang="en">
<head>
<meta charset="utf-8">
<title>Kelt Athletic — Business Card</title>
<link rel="stylesheet" href="https://fonts.googleapis.com/css2?family=Roboto:wght@400;500;700&display=swap">
<style>
  :root {
    --backdrop: #3d3d3d;
    --card: #ffffff;
    --ink: #111111;
    --text-grey: #555555;
    --accent-red: #e31e24;
    --brand-grey: #8a8a8a;
    --brand-plum: #5e4a66;
  }
  * { box-sizing: border-box; margin: 0; padding: 0; }
  html, body {
    width: 1105px; height: 1200px; overflow: hidden;
    background: var(--backdrop);
    font-family: "Roboto", Arial, sans-serif;
  }
  .card {
    position: absolute; left: 196px; width: 720px; height: 412px;
    background: var(--card);
  }
  .card--front { top: 146px; }
  .card--back { top: 602px; height: 410px; }

  .front-band {
    position: absolute; left: 0; top: 74px; width: 290px; height: 34px;
    background: var(--ink);
  }
  .front-wordmark {
    position: absolute; left: 312px; top: 64px;
    font-size: 44px; font-weight: 500; color: var(--ink); letter-spacing: 0.5px;
    line-height: 1;
  }

  .holder { position: absolute; left: 52px; top: 260px; }
  .holder-name { font-size: 26px; font-weight: 700; color: var(--accent-red); }
  .holder-role { font-size: 19px; color: var(--ink); margin-top: 4px; }

  .address {
    position: absolute; right: 49px; top: 215px; text-align: right;
    font-size: 19px; line-height: 26px; color: var(--text-grey);
  }
  .contact {
    position: absolute; right: 49px; top: 280px; list-style: none;
    font-size: 19px; line-height: 27.5px; color: var(--text-grey);
  }
  .contact li { display: flex; justify-content: flex-end; align-items: center; gap: 8px; }
  .contact svg { width: 18px; height: 18px; flex: none; }

  .back-wordmark {
    position: absolute; left: 0; right: 0; top: 148px; text-align: center;
    font-size: 64px; font-weight: 500; color: var(--ink); line-height: 1;
  }
  .brand-row {
    position: absolute; left: 0; right: 0; top: 326px;
    display: flex; justify-content: center; align-items: center; gap: 26px;
    list-style: none; font-size: 20px; font-weight: 500;
  }
  .brand--pawaluni { color: var(--brand-grey); }
  .brand--verdantflex { color: var(--brand-plum); }
  .brand--gritgale { color: var(--accent-red); }
  .brand--kelt { color: var(--ink); }
</style>
</head>
<body>
  <section class="card card--front" aria-label="Card front">
    <div class="front-band"></div>
    <div class="front-wordmark">Kelt Athletic</div>

    <div class="holder">
      <p class="holder-name">Ewan Marchetti</p>
      <p class="holder-role">Managing Director</p>
    </div>

    <address class="address">
      Ferris Court, Oakby<br>
      Harwell, ZZ9 4QT
    </address>

    <ul class="contact">
      <li>+44 (0)1632 960418
        <svg viewBox="0 0 24 24" aria-hidden="true"><path fill="#e31e24" d="M6.6 10.8a15.1 15.1 0 0 0 6.6 6.6l2.2-2.2a1 1 0 0 1 1-.25 11.4 11.4 0 0 0 3.6.57 1 1 0 0 1 1 1V20a1 1 0 0 1-1 1A17 17 0 0 1 3 4a1 1 0 0 1 1-1h3.5a1 1 0 0 1 1 1c0 1.25.2 2.45.57 3.6a1 1 0 0 1-.25 1z"/></svg>
      </li>
      <li>ewan@keltathletic.co.uk
        <svg viewBox="0 0 24 24" aria-hidden="true"><rect x="2" y="5" width="20" height="14" fill="#e31e24"/><path d="M2 5l10 8 10-8" fill="none" stroke="#fff" stroke-width="1.6"/></svg>
      </li>
      <li>www.keltathletic.co.uk
        <svg viewBox="0 0 24 24" aria-hidden="true"><circle cx="12" cy="12" r="10" fill="#e31e24"/><path d="M2 12h20M12 2c3 3 3 17 0 20M12 2c-3 3-3 17 0 20" fill="none" stroke="#fff" stroke-width="1.4"/></svg>
      </li>
    </ul>
  </section>

  <section class="card card--back" aria-label="Card back">
    <div class="back-wordmark">Kelt Athletic</div>
    <ul class="brand-row">
      <li class="brand--pawaluni">PawaLuni</li>
      <li class="brand--verdantflex">VerdantFlex</li>
      <li class="brand--gritgale">Grit and Gale</li>
      <li class="brand--kelt">Kelt</li>
    </ul>
  </section>
</body>
</html>
```